We need a design for a contracting company website based in KSA, something modern with the same color theme as the attached logo. including a page for people who want to submit their CV and try to apply for a job.Also to include the "about us, contact us, gallery, Divisions, Supplies, etc...". If possible to have an interactive or moving background. Please disregard the "Bright Pathways" Section in the attached profile.

Industry/Entity Type

Construction Company

Number of Pages Required

5+ page

Colors

Designer to choose colors to be used in the design.

Requirements
Must have
• Pages:
• about us, contact us, gallery, Divisions, Apply for a job, Supplies
Nice to have
• - Moving or interactive background

```html
<!DOCTYPE html>
<html lang="en">
<head>
<meta charset="utf-8">
<title>Cobaltine Building Company — About Us</title>
<link href="https://fonts.googleapis.com/css2?family=Roboto:wght@300;400;500;700&family=Josefin+Sans:wght@400;600;700&display=swap" rel="stylesheet">
<style>
:root{
  --yellow:#f2c811;
  --yellow-soft:#f6dc6a;
  --dark:#2e2e2e;
  --ink:#222;
  --muted:#6b6b6b;
  --navy:#2b303c;
  --navy-deep:#232733;
  --line:#e4e4e4;
  --white:#fff;
}
*{box-sizing:border-box;margin:0;padding:0}
html,body{width:1200px;height:4468px;overflow:hidden}
body{position:relative;background:var(--white);font-family:'Roboto',sans-serif;color:var(--ink)}
.abs{position:absolute}
.center{text-align:center}

/* header */
.brand{left:203px;top:14px;display:flex;align-items:center;gap:10px}
.brand-mark{width:30px;height:54px;background:var(--yellow)}
.brand-name{font-family:'Josefin Sans',sans-serif;font-weight:600;font-size:17px;line-height:19px;color:var(--ink);width:150px}
.nav{left:553px;top:52px;display:flex;gap:22px;font-size:10px;color:#444;align-items:center}
.nav .active{background:var(--dark);color:#fff;padding:5px 8px}
.nav svg{margin-left:2px}

/* hero */
.hero{left:53px;top:91px;width:1094px;height:507px;background:linear-gradient(160deg,#3d5d86 0%,#2b4470 45%,#6a6d6e 75%,#2c3d5e 100%)}
.hero-title{left:53px;top:240px;width:1094px;font-family:'Josefin Sans',sans-serif;font-weight:700;font-size:52px;color:#fff;letter-spacing:1px}
.hero-text{left:255px;top:310px;width:690px;font-size:15px;line-height:19px;color:#fff}
.btn-grey{left:549px;top:392px;width:107px;height:29px;background:#d8d8d8;border-radius:5px;font-size:10px;font-weight:700;line-height:29px;color:#333}

.tabs{left:162px;top:598px;width:876px;height:79px;background:var(--dark);display:flex;align-items:center;color:#fff;font-family:'Josefin Sans',sans-serif;font-weight:700;font-size:19px}
.tabs span{flex:1;text-align:center}
.tabs .on{text-decoration:underline;text-decoration-color:var(--yellow);text-decoration-thickness:3px;text-underline-offset:8px}
.tabs .sep{flex:0 0 1px;height:34px;background:#666}

/* activities */
.map{left:53px;top:720px;width:550px;height:290px;background:radial-gradient(ellipse at 40% 50%,#e3e3e3,#f7f7f7 70%)}
.photo-tools{left:203px;top:794px;width:159px;height:157px;background:linear-gradient(135deg,#c79a2a,#6e6e6e)}
.photo-frame{left:388px;top:734px;width:158px;height:157px;background:linear-gradient(160deg,#f2c811,#b98410)}
.photo-bridge{left:330px;top:920px;width:95px;height:94px;border:5px solid var(--yellow);background:linear-gradient(180deg,#d7a24a,#7a5b3a)}
.sq{background:#1f1f1f}
.act-list{left:636px;top:736px;width:400px;font-family:'Josefin Sans',sans-serif;font-size:12.5px;line-height:20px;color:#444}
.act-list p{margin-bottom:20px}
.act-list p.tight{margin-bottom:0}
.rule{left:53px;top:1066px;width:970px;height:1px;background:var(--line)}

/* section heading */
.eyebrow{font-size:11px;letter-spacing:3px;color:#555}
.eyebrow::before,.eyebrow::after{content:"";display:inline-block;width:110px;border-top:1px dashed #888;vertical-align:middle;margin:0 14px}
.h2{font-size:27px;font-weight:700;color:var(--ink);letter-spacing:-.5px}
.h2 em{font-style:normal;color:var(--yellow)}
.sub{font-size:10px;line-height:16px;color:#777}

.filters{left:0;top:1210px;width:1200px;display:flex;justify-content:center;gap:20px;font-size:10.5px;color:#555}
.filters .on{color:var(--yellow)}
.tile{top:1243px;width:274px;height:274px}
.t1{left:53px;background:linear-gradient(160deg,#a9a9a4,#5b5246 60%,#3a3530)}
.t2{left:327px;background:linear-gradient(160deg,#f3d21a,#d7b20e 60%,#c9a40e)}
.t3{left:601px;background:linear-gradient(160deg,#90a6b8,#c9a36a 55%,#6b6b6b)}
.t4{left:875px;background:linear-gradient(180deg,#56604a,#8a8650 55%,#3a3d2c)}
.circle-ic{width:30px;height:30px;border:1.5px solid #fff;border-radius:50%}
.btn-yellow{background:var(--yellow);color:#2a2a2a;font-size:11px;font-weight:700;text-align:center;border-radius:2px}

/* civil works */
.civil{left:53px;top:1629px;width:1094px;height:564px;background:linear-gradient(180deg,#f2cb12,#e9c20f)}
.civil-card{top:1835px;width:256px;height:255px;text-align:center;padding-top:50px}
.cc1{left:272px;background:var(--yellow-soft)}
.cc2{left:650px;border:3px double #fff;background:rgba(255,255,255,.08)}
.civil-card h3{font-size:15px;font-weight:700;margin:18px 0 10px;color:#222}
.civil-card p{font-size:10.5px;line-height:17px;color:#444;padding:0 22px}
.cc2 p{color:#b8a04c}
.civil-card .more{font-size:10.5px;font-weight:700;margin-top:8px;color:#222}

/* ict */
.ict{left:53px;top:2193px;width:1094px;height:556px}
.ict-title{left:53px;top:2275px;width:1094px;font-size:24px;font-weight:700;color:#fff;letter-spacing:-.3px}
.ict-item{width:230px}
.ict-item h4{font-size:11px;color:var(--yellow);font-weight:500;margin-bottom:7px}
.ict-item p{font-size:10px;line-height:16px;color:#ddd}
.ict-ic{width:22px;height:22px;background:var(--yellow);border-radius:4px}

/* team */
.card-y{top:2945px;width:238px;height:320px;background:var(--yellow);padding:13px}
.card-y .inner{width:100%;height:100%;background:#fff}
.person{background:linear-gradient(180deg,#f5f5f5 0%,#e8c36a 40%,#c08a3a 100%)}
.card-d{left:482px;top:2945px;width:239px;height:320px;background:#3a3a3a;padding:12px}
.card-d .inner{width:100%;height:100%;background:rgba(242,200,17,.92);padding:20px 18px;color:#fff}
.dots{left:545px;top:3303px;display:flex;gap:8px}
.dots i{display:block;width:16px;height:3px;background:var(--yellow)}
.dots i.on{background:#333;width:22px}

/* testimonials */
.testi{left:53px;top:3371px;width:1094px;height:537px;background:linear-gradient(135deg,#3e4a5a,#2b2f35 50%,#5a4a36)}
.testi-card{left:372px;top:3576px;width:457px;height:206px;background:#fff;border-radius:8px;padding:30px 70px}
.brands{left:201px;top:3865px;width:800px;height:86px;background:#fff;box-shadow:0 4px 14px rgba(0,0,0,.12);display:flex;align-items:center;justify-content:space-around;font-size:26px;font-weight:700;color:#333}
.brands span{display:flex;align-items:center;gap:8px}
.brands i{display:block;width:14px;height:14px;background:var(--yellow)}

/* footer */
.footer{left:53px;top:3990px;width:1094px;height:478px;background:var(--navy)}
.f-h{font-size:16px;color:#fff;font-weight:400}
.f-txt{font-size:9.5px;line-height:17px;color:#dcdcdc}
.f-links{list-style:none;font-size:9.5px;line-height:20.5px;color:#dcdcdc}
.f-links li::before{content:"›";margin-right:10px}
.soc{width:26px;height:26px;border-radius:50%;background:#fff}
.date{width:32px;height:32px;border:1.5px solid #fff;border-radius:50%;font-size:9px;color:#fff;text-align:center;line-height:11px;padding-top:5px}
.copy{left:53px;top:4392px;width:1094px;font-size:10px;color:#dcdcdc}
</style>
</head>
<body>

<!-- header -->
<div class="abs brand"><div class="brand-mark"></div><div class="brand-name">Cobaltine Building Company</div></div>
<nav class="abs nav">
  <span class="active">About Us</span><span>Projects</span><span>Services</span><span>Plan</span><span>Testimonials</span><span>Latest News</span><span>Contact Us</span>
  <svg width="13" height="13" viewBox="0 0 13 13"><circle cx="5.5" cy="5.5" r="4" fill="none" stroke="#222" stroke-width="1.8"/><line x1="8.5" y1="8.5" x2="12" y2="12" stroke="#222" stroke-width="1.8"/></svg>
</nav>

<!-- hero -->
<div class="abs hero" role="img" aria-label="Photo of a construction worker in a hard hat shaking hands"></div>
<h1 class="abs hero-title center">ABOUT US</h1>
<p class="abs hero-text center">Nemo enim ipsam voluptatem quia voluptas sit aspernatur aut odit aut fugit, sed quia consequuntur magni dolores eos qui ratione voluptatem sequi nesciunt. Neque porro quisquam est, qui dolorem ipsum quia dolor sit amet, consectetur, adipisci velit,</p>
<div class="abs btn-grey center">VIEW ALL</div>

<div class="abs tabs"><span class="on">SPECIALIZED ACTIVITIES</span><span class="sep"></span><span>TRADING DIVISION</span></div>

<!-- activities -->
<div class="abs map" role="img" aria-label="Dotted world map"></div>
<div class="abs photo-tools" role="img" aria-label="Photo of hand tools on a tool belt"></div>
<div class="abs photo-frame" role="img" aria-label="Photo of a timber building frame under construction"></div>
<div class="abs photo-bridge" role="img" aria-label="Photo of a bridge structure"></div>
<div class="abs sq" style="left:445px;top:915px;width:43px;height:41px"></div>
<div class="abs sq" style="left:292px;top:966px;width:23px;height:23px"></div>
<div class="abs act-list">
  <p>1- Waterproofing activities including (All kind of waterproofing such as Bituminous, Elastic Membrane, Liquid Applied and Sprayed waterproofing)</p>
  <p>2- Expansion Joint (Supply &amp; Apply) a. Construction Joints b. Control Joints</p>
  <p>3- Dry wall and ceiling (Supply and Apply) a. Specialized for specific requirements for Fire, Sound and Heights</p>
  <p class="tight">4- Concrete Repair</p>
  <p>5- Industrial Flooring (Epoxy, Polyurethane, etc…)</p>
</div>
<div class="abs rule"></div>

<!-- projects -->
<div class="abs center" style="left:0;top:1090px;width:1200px">
  <div class="eyebrow">OUR PROJECTS</div>
  <div class="h2" style="margin-top:2px">VIEW OUR <em>PROJECTS GALLERY</em></div>
  <div class="sub" style="margin-top:8px">Lorem ipsum dolor sit amet, consectetur adipiscing elit, sed do eiusmod tempor incididunt ut labore et dolore magna<br>Quis nostrud exercitation ullamco laboris nisi ut aliquip ex ea commodo consequat.</div>
</div>
<div class="abs filters"><span class="on">All</span><span>Constructions</span><span>Architecture</span><span>Building</span><span>Interior</span><span>Renovation</span></div>
<div class="abs tile t1" role="img" aria-label="Photo of a loader on a building site"></div>
<div class="abs tile t2" role="img" aria-label="Photo of a welder at work, yellow overlay"></div>
<div class="abs tile t3" role="img" aria-label="Photo of two builders in hard hats working"></div>
<div class="abs tile t4" role="img" aria-label="Photo of tower cranes at sunset"></div>
<div class="abs circle-ic" style="left:334px;top:1478px"></div>
<div class="abs circle-ic" style="left:372px;top:1478px"></div>
<svg class="abs" style="left:100px;top:1391px" width="30" height="30" viewBox="0 0 30 30"><circle cx="15" cy="15" r="13" fill="none" stroke="#fff" stroke-width="1.5"/><path d="M17 9l-6 6 6 6" fill="none" stroke="#fff" stroke-width="1.5"/></svg>
<svg class="abs" style="left:1070px;top:1391px" width="30" height="30" viewBox="0 0 30 30"><circle cx="15" cy="15" r="13" fill="none" stroke="#fff" stroke-width="1.5"/><path d="M13 9l6 6-6 6" fill="none" stroke="#fff" stroke-width="1.5"/></svg>
<div class="abs btn-yellow" style="left:521px;top:1558px;width:158px;height:42px;line-height:42px">SEE ALL WORKS &nbsp;→</div>

<!-- civil works -->
<div class="abs civil" role="img" aria-label="Faint photo of a construction site behind a yellow tint"></div>
<div class="abs center" style="left:0;top:1683px;width:1200px">
  <div class="eyebrow">WE ARE SKILLED FOR</div>
  <div class="h2" style="font-size:24px;font-weight:500">CIVIL WORKS</div>
  <div class="sub" style="margin-top:26px;color:#8a7412">Cobaltine Building Company (CBC) undertakes a range of civil works projects and takes pride<br>Construct and Local Government sectors. Our highly skilled work crews<br>delivered safely, on time and within budget.</div>
</div>
<div class="abs civil-card cc1">
  <svg width="34" height="38" viewBox="0 0 34 38"><path d="M11 2h12l-4 8h-4z" fill="#222"/><path d="M17 10c-9 4-14 12-14 18 0 6 5 8 14 8s14-2 14-8c0-6-5-14-14-18z" fill="#222"/><text x="17" y="30" font-size="13" font-family="Roboto,sans-serif" font-weight="700" fill="#f6dc6a" text-anchor="middle">$</text></svg>
  <h3>GENERAL ACTIVITY</h3>
  <p>Lorem ipsum dolor sit am consecteturadipiscing elit. sed do eiusmod tempor incididunt ut labore aliquip ex ea commodo consequat.</p>
  <div class="more">READ MORE &nbsp;→</div>
</div>
<div class="abs civil-card cc2">
  <svg width="28" height="38" viewBox="0 0 28 38"><path d="M14 2c6 6 8 14 6 24H8C6 16 8 8 14 2z" fill="#222"/><circle cx="14" cy="15" r="3" fill="#f2c811"/><path d="M8 22l-5 8h6zM20 22l5 8h-6z" fill="#222"/><path d="M11 28h6l-3 8z" fill="#222"/></svg>
  <h3>SPECIALIZED ACTIVITY</h3>
  <p>Lorem ipsum dolor sit am consecteturadipiscing elit. sed do eiusmod tempor incididunt ut labore aliquip ex ea commodo consequat.</p>
  <div class="more">READ MORE &nbsp;→</div>
</div>

<!-- ict solutions -->
<svg class="abs ict" viewBox="0 0 1094 556" preserveAspectRatio="none" role="img" aria-label="Dark photo of a worker with cranes in the background">
  <defs><linearGradient id="ictbg" x1="0" y1="0" x2="1" y2="1"><stop offset="0" stop-color="#2a2a28"/><stop offset=".6" stop-color="#35342e"/><stop offset="1" stop-color="#4a4638"/></linearGradient></defs>
  <path d="M0 0H1094V470Q547 570 0 470Z" fill="url(#ictbg)"/>
</svg>
<div class="abs ict-title center"><span style="display:inline-block;width:44px;border-top:1px dashed #ccc;vertical-align:middle;margin-right:6px"></span>ICT SOLUTIONS<span style="display:inline-block;width:44px;border-top:1px dashed #ccc;vertical-align:middle;margin-left:6px"></span></div>

<div class="abs ict-ic" style="left:188px;top:2347px"></div>
<div class="abs ict-item" style="left:235px;top:2354px"><h4>INTERCOM SYSTEMS</h4><p>Duis aute irure dolor in reprehenderit in voluptate velit esse cillum dolore euxas nulla Excepteur pariatur.</p></div>
<div class="abs ict-ic" style="left:474px;top:2347px;border-radius:50%"></div>
<div class="abs ict-item" style="left:521px;top:2354px"><h4>MASTER CLOCK SYSTEMS</h4><p>Duis aute irure dolor in reprehenderit in voluptate velit esse cillum dolore euxas nulla Excepteur pariatur.</p></div>
<div class="abs ict-ic" style="left:760px;top:2347px"></div>
<div class="abs ict-item" style="left:807px;top:2354px"><h4>VIDEO WALL AND DISPLAY</h4><p>Duis aute irure dolor in reprehenderit in voluptate velit esse cillum dolore euxas nulla Excepteur pariatur.</p></div>
<div class="abs ict-ic" style="left:188px;top:2488px"></div>
<div class="abs ict-item" style="left:235px;top:2495px"><h4>WIRELESS LAN</h4><p>Duis aute irure dolor in reprehenderit in voluptate velit esse cillum dolore euxas nulla Excepteur pariatur.</p></div>
<div class="abs ict-ic" style="left:474px;top:2488px"></div>
<div class="abs ict-item" style="left:521px;top:2495px"><h4>VOIP MANAGEMENT</h4><p>Duis aute irure dolor in reprehenderit in voluptate velit esse cillum dolore euxas nulla Excepteur pariatur.</p></div>
<div class="abs btn-yellow" style="left:526px;top:2620px;width:146px;height:41px;line-height:41px">VIEW ALL</div>

<!-- team -->
<div class="abs center" style="left:0;top:2822px;width:1200px">
  <div class="eyebrow" style="font-size:12px">WE HAVE CREATIVE</div>
  <div class="h2" style="font-size:26px;margin-top:2px">EXPERT <em>TEAM MEMBERS</em></div>
  <div class="sub" style="margin-top:8px">Dolore magna Quis nostrud exercitation ullamco laboris nisi ut aliquip ex ea commodo consequat</div>
</div>
<div class="abs card-y" style="left:201px"><div class="inner person" role="img" aria-label="Photo of a female builder in hard hat and overalls"></div></div>
<div class="abs card-d">
  <div class="inner">
    <div style="font-size:15px;font-weight:700">KARIM <span style="font-weight:300">OSTEN</span></div>
    <div style="font-size:8px;margin-top:3px">SR. ARCHITECT</div>
    <div style="display:flex;gap:5px;margin-top:220px"><i style="width:12px;height:12px;border:1px solid #fff;border-radius:50%"></i><i style="width:12px;height:12px;border:1px solid #fff;border-radius:50%"></i><i style="width:12px;height:12px;border:1px solid #fff;border-radius:50%"></i><i style="width:12px;height:12px;border:1px solid #fff;border-radius:50%"></i></div>
  </div>
</div>
<div class="abs card-y" style="left:762px"><div class="inner person" role="img" aria-label="Photo of a male builder in hard hat with rope"></div></div>
<div class="abs dots"><i></i><i class="on"></i><i></i><i></i><i></i></div>

<!-- testimonials -->
<div class="abs testi" role="img" aria-label="Dark photo of a worker holding a power drill"></div>
<div class="abs center" style="left:0;top:3450px;width:1200px;color:#fff">
  <div class="eyebrow" style="color:#eee">CLIENTS FEEDBACK</div>
  <div class="h2" style="color:#fff;font-size:25px">CLIENT TESTIMONIALS</div>
  <div class="sub" style="color:#ddd;margin-top:4px">Dolore magna Quis nostrud exercitation ullamco laboris nisi ut aliquip<br>ex ea commodo consequat</div>
</div>
<div class="abs testi-card">
  <div style="display:flex;align-items:center;gap:16px"><span style="width:30px;height:30px;border-radius:50%;background:#111;display:block"></span><div><div style="font-size:11px;font-weight:700">SAMI HARLOW</div><div style="font-size:7px;color:#888">CONTRACTOR</div></div></div>
  <p style="font-size:9.5px;line-height:15px;font-style:italic;color:#888;margin-top:22px">It is a long established fact that a reader will be distracted readable content of a page when looking at its layout. The point of using rem Ipsum is that it has a look like readable English.</p>
  <div style="color:var(--yellow);font-size:10px;margin-top:6px;letter-spacing:2px">★★★★★</div>
</div>
<svg class="abs" style="left:305px;top:3669px" width="28" height="28" viewBox="0 0 28 28"><circle cx="14" cy="14" r="12" fill="none" stroke="#fff" stroke-width="1.3"/><path d="M16 9l-5 5 5 5" fill="none" stroke="#fff" stroke-width="1.3"/></svg>
<svg class="abs" style="left:858px;top:3669px" width="28" height="28" viewBox="0 0 28 28"><circle cx="14" cy="14" r="12" fill="none" stroke="#fff" stroke-width="1.3"/><path d="M12 9l5 5-5 5" fill="none" stroke="#fff" stroke-width="1.3"/></svg>
<div class="abs brands"><span><i></i>Norvex</span><span><i></i>Kestrali</span><span>Soluvia</span><span><i style="border-radius:50%"></i>Meridio</span></div>

<!-- footer -->
<div class="abs footer"></div>
<div class="abs" style="left:203px;top:4083px;width:195px">
  <div class="f-h">About Company</div>
  <div style="font-size:13px;font-weight:700;color:#fff;margin-top:18px">CONSTRUCTION</div>
  <p class="f-txt" style="margin-top:4px">CBC (Previously Al-Varesh) was established in the year 1980 as a sub-contractor Specialized in waterproofing and specialized finishing, with the main target of furnishing the Saudi market by a professional team of engineers and applicators to</p>
  <div style="display:flex;gap:14px;margin-top:18px"><i class="soc"></i><i class="soc"></i><i class="soc"></i><i class="soc"></i><i class="soc"></i></div>
</div>
<div class="abs" style="left:447px;top:4083px">
  <div class="f-h">Explor link</div>
  <ul class="f-links" style="margin-top:18px"><li>Our services</li><li>Meet our team</li><li>Forum</li><li>Help center</li><li>Contact Cobaltine</li><li>Privacy Policy</li><li>Cobaltine terms</li><li>Site map</li></ul>
</div>
<div class="abs" style="left:625px;top:4083px;width:190px">
  <div class="f-h">Latest post</div>
  <div style="margin-top:18px;display:flex;flex-direction:column;gap:18px">
    <div style="display:flex;gap:12px"><div class="date">20<br>AUG</div><p class="f-txt" style="line-height:15px">Luptatum omittantur duo ne mpetus indoctum</p></div>
    <div style="display:flex;gap:12px"><div class="date">20<br>AUG</div><p class="f-txt" style="line-height:15px">Luptatum omittantur duo ne mpetus indoctum</p></div>
    <div style="display:flex;gap:12px"><div class="date">20<br>AUG</div><p class="f-txt" style="line-height:15px">Luptatum omittantur duo ne mpetus indoctum</p></div>
    <div style="display:flex;gap:12px"><div class="date">20<br>AUG</div><p class="f-txt" style="line-height:15px">Luptatum omittantur duo ne mpetus indoctum</p></div>
  </div>
</div>
<div class="abs" style="left:853px;top:4083px;width:260px">
  <div class="f-h">Contact us</div>
  <div style="display:flex;gap:14px;margin-top:20px">
    <svg width="10" height="14" viewBox="0 0 10 14"><path d="M5 0a5 5 0 0 1 5 5c0 4-5 9-5 9S0 9 0 5a5 5 0 0 1 5-5z" fill="#fff"/><circle cx="5" cy="5" r="2" fill="#2b303c"/></svg>
    <p class="f-txt" style="line-height:15px">COBALTINE BUILDING COMPANY<br>Coral Avenue - Harbor District<br>4410 Jeddah 21000 KSA</p>
  </div>
  <div style="display:flex;gap:14px;margin-top:28px;align-items:center">
    <svg width="12" height="9" viewBox="0 0 12 9"><rect width="12" height="9" fill="#fff"/><path d="M0 0l6 5 6-5" fill="none" stroke="#2b303c"/></svg>
    <p class="f-txt">info@cobaltine-build.com</p>
  </div>
  <div style="display:flex;gap:14px;margin-top:14px">
    <svg width="9" height="14" viewBox="0 0 9 14"><rect width="9" height="14" rx="1.5" fill="#fff"/><rect x="1.5" y="2" width="6" height="8" fill="#2b303c"/></svg>
    <p class="f-txt" style="line-height:15px">00 966 (12) 555 0142<br>00 966 12 555 0178</p>
  </div>
</div>
<div class="abs copy center">Copyright @ 2019 | Designed By Northwind Studio</div>

</body>
</html>
```